Landing page for B2B Product Idea Validation Event

We need a single landing page design for the world’s first competition to help aspiring entrepreneurs to validate their new business 2 business (B2B) web application ideas.

We like the following landing pages as examples for the structure and sectioning we would like to see for this landing page:
http://ny.vexorlane.com/
https://trelvo.com/trelvocon

There should be around 5 sections including an application form.

Target Market(s)

Entrepreneurs

Industry/Entity Type

Business Software

Number of Pages Required

1 page

Font styles to use
Serif

Requirements
Must have
• Colors must be similar to the logo provided.

```html
<!DOCTYPE html>
<html lang="en">
<head>
<meta charset="utf-8">
<title>Bizlaunch – Start Differently</title>
<link rel="stylesheet" href="https://fonts.googleapis.com/css2?family=Raleway:wght@400;500;600;700&family=Open+Sans:wght@400;600&display=swap">
<style>
:root{
  --blue:#2f6fd6;
  --blue-deep:#1f5cc4;
  --navy:#10307a;
  --navy-line:#2c4a91;
  --ink:#333a44;
  --muted:#8a8f96;
  --soft:#efefef;
  --soft-2:#e6e6e6;
  --gold:#f2c443;
  --white:#ffffff;
}
*{margin:0;padding:0;box-sizing:border-box}
html,body{width:1200px;height:3169px;overflow:hidden}
body{font-family:"Open Sans",Arial,sans-serif;color:var(--ink);background:var(--white);position:relative}
h2,h3,.nav a,.brand{font-family:"Raleway",Arial,sans-serif}
section,header,footer{position:absolute;left:0;width:1200px}
.center{text-align:center}

/* hero */
.hero{top:0;height:530px;overflow:hidden}
.hero-photo{position:absolute;inset:0;background:radial-gradient(ellipse at 25% 40%,#4a5f88 0%,#2b3550 35%,#6a3a32 70%,#3a2a2a 100%)}
.hero-shade{position:absolute;inset:0;background:linear-gradient(180deg,rgba(10,20,40,.35),rgba(10,20,40,.2))}
.brand{position:absolute;left:137px;top:28px;font-size:32px;font-weight:700;color:var(--white);letter-spacing:.5px}
.nav{position:absolute;top:36px;right:148px;display:flex;gap:38px}
.nav a{color:var(--white);text-decoration:none;font-size:15px;font-weight:500;letter-spacing:.5px}
.hero-sub{position:absolute;top:205px;left:0;width:100%;color:var(--white);font-family:"Raleway",sans-serif;font-size:25px;line-height:29px;text-align:center}
.hero-title{position:absolute;top:262px;left:0;width:100%;color:var(--white);font-family:"Raleway",sans-serif;font-weight:700;font-size:68px;letter-spacing:2px;text-align:center}
.hero-curve{position:absolute;left:0;bottom:0}
.dots{position:absolute;top:500px;left:556px;display:flex;gap:6px}
.dots span{width:18px;height:18px;border-radius:50%;background:var(--white)}
.dots span:first-child{background:transparent;border:2px solid var(--white)}

/* about */
.about{top:530px;height:241px}
.about h2{font-size:35px;font-weight:400;color:var(--ink);margin-top:53px}
.lede{font-size:13px;line-height:25px;color:var(--muted);width:780px;margin:18px auto 0}

/* eligibility */
.eligibility{top:771px;height:332px;background:var(--soft)}
.eligibility h2{font-size:29px;font-weight:500;letter-spacing:1px;margin-top:52px}
.eligibility .tagline{font-size:17px;color:var(--muted);margin-top:24px}
.eligibility .lede{font-size:12px;line-height:21px;width:780px;margin-top:12px}
.criteria{display:flex;justify-content:center;gap:80px;margin-top:30px;font-family:"Raleway",sans-serif;font-size:16px;color:var(--blue)}
.criteria b{font-weight:700}

/* application */
.application{top:1103px;height:389px;overflow:hidden}
.application .bg{position:absolute;inset:0;background:linear-gradient(120deg,#3b7ae0,#2a66cf 50%,#2f70d8)}
.application h2{position:relative;color:var(--white);font-size:29px;font-weight:500;letter-spacing:1px;margin-top:40px}
.steps{position:absolute;top:106px;left:0;width:100%}
.step{position:absolute;width:270px;margin-left:-135px;text-align:center;color:var(--white)}
.step .ring{width:118px;height:118px;margin:0 auto;border:2px solid rgba(255,255,255,.9);border-radius:50%;display:flex;align-items:center;justify-content:center}
.step .ring span{width:100px;height:100px;border-radius:50%;background:var(--navy);display:flex;align-items:center;justify-content:center}
.step h3{font-size:18px;font-weight:500;margin-top:26px;letter-spacing:.5px}
.step p{font-size:11.5px;line-height:21px;color:rgba(255,255,255,.75);margin-top:8px}

/* prize */
.prize{top:1492px;height:308px;overflow:hidden}
.prize .bg{position:absolute;inset:0;background:linear-gradient(90deg,#6c5a4a,#a08c78 40%,#8a7e72 70%,#5e564e)}
.prize .bg::after{content:"";position:absolute;inset:0;background:rgba(40,35,30,.35)}
.prize .inner{position:relative;color:var(--white)}
.prize h2{font-size:27px;font-weight:700;margin-top:68px;letter-spacing:.5px}
.prize p{font-size:18px;line-height:29px;width:520px;margin:8px auto 0}
.prize .amount{font-family:"Raleway",sans-serif;font-size:42px;font-weight:600;color:var(--gold);margin-top:10px}

/* judges */
.judges{top:1800px;height:355px;background:var(--soft-2)}
.judges h2{font-size:26px;font-weight:600;letter-spacing:1px;margin-top:37px}
.judge{position:absolute;top:92px;width:180px;margin-left:-90px;text-align:center}
.judge .frame{width:150px;height:150px;margin:0 auto;border-radius:50%;background:var(--white);padding:7px;box-shadow:0 1px 4px rgba(0,0,0,.15)}
.judge .portrait{width:136px;height:136px;border-radius:50%;background:linear-gradient(180deg,#c8ccd2,#7f8a99)}
.judge h3{font-size:14px;font-weight:700;color:var(--blue);margin-top:22px}
.judge .co{display:flex;justify-content:center;align-items:center;gap:14px;font-size:11.5px;color:var(--muted);margin-top:6px}
.judge .co i{width:18px;height:18px;background:var(--blue-deep);border-radius:2px}

/* faq */
.faq{top:2155px;height:427px}
.faq h2{font-size:29px;font-weight:500;color:var(--blue);margin-top:32px}
.faq-list{position:absolute;top:89px;left:222px;width:758px;border:1px solid #d4d6da}
.faq-q{display:flex;align-items:center;height:42px;padding:0 16px 0 18px;font-size:14px;color:var(--ink);border-top:1px solid #d4d6da}
.faq-q b{font-weight:400;width:34px;font-size:16px}
.faq-q span{flex:1}
.faq-q svg{flex:none}
.faq-q.open{background:var(--blue);color:var(--white);border-top:none}
.faq-a{display:flex;padding:14px 20px 14px 18px;font-size:11.5px;line-height:20px;color:#555}
.faq-a b{font-weight:400;width:34px;font-size:16px;color:var(--blue)}
.faq-a span{flex:1}

/* sponsors */
.sponsors{top:2582px;height:260px;background:var(--soft)}
.sponsors h2{font-size:27px;font-weight:700;letter-spacing:1px;margin-top:36px;color:#222}
.sponsor-row{position:absolute;top:128px;left:165px;width:910px;display:flex;justify-content:space-between;align-items:center}
.sponsor-row span{font-family:"Raleway",sans-serif;font-size:21px;font-weight:600;color:#9ea2a8}

/* footer */
.site-footer{top:2842px;height:327px;background:var(--navy);color:var(--white)}
.col{position:absolute;top:52px}
.col h3{font-size:17px;font-weight:500;letter-spacing:.5px;margin-bottom:14px}
.col a{display:block;color:var(--white);text-decoration:none;font-size:12px;line-height:28.5px}
.col p{font-size:12px;margin-bottom:14px}
.signup input{display:block;width:247px;height:34px;border:none;padding:0 12px;font-size:11px;font-family:inherit}
.signup button{margin-top:14px;width:110px;height:32px;border:none;background:var(--blue);color:var(--white);font-size:12px;font-weight:600;font-family:inherit}
.socials{display:flex;gap:12px}
.socials i{width:34px;height:34px;border-radius:50%;background:#6b7fa9}
.partner{font-family:"Raleway",sans-serif;font-size:26px;font-weight:600;color:var(--white);margin-top:30px}
.rule{position:absolute;top:258px;left:140px;width:922px;height:1px;background:var(--navy-line)}
.copy{position:absolute;top:282px;left:0;width:100%;text-align:center;font-size:11px;color:rgba(255,255,255,.8)}
</style>
</head>
<body>

<header class="hero">
  <div class="hero-photo" role="img" aria-label="Speaker presenting on stage to a seated conference audience"></div>
  <div class="hero-shade"></div>
  <div class="brand">Bizlaunch</div>
  <nav class="nav"><a href="#about">ABOUT</a><a href="#">CONFERENCE</a><a href="#">EVENT</a><a href="#">SPEAKERS</a><a href="#">SCHEDULE</a></nav>
  <p class="hero-sub">World’s first competition to help aspiring entrepreneurs to validate<br>their new business 2 business (B2B) ideas</p>
  <h1 class="hero-title">START DIFFERENTLY</h1>
  <svg class="hero-curve" width="1200" height="60" viewBox="0 0 1200 60" aria-hidden="true"><path d="M0 22 Q600 66 1200 22 L1200 60 L0 60 Z" fill="#fff"/></svg>
  <div class="dots"><span></span><span></span><span></span><span></span></div>
</header>

<section class="about center" id="about">
  <h2>About Bizlaunch</h2>
  <p class="lede">Praesent elementum elit at tellus nec ultricies sit amet porttitor mattis enim In massa libero interdum nec interdum vel blandit sed nulla In ullamcorper est eget tempor cursus neque mi consectetuer mi a ultricies massa est sed nisl Class aptent taciti sociosqu ad litora torquent per conubia nostra per inceptos</p>
</section>

<section class="eligibility center">
  <h2>ELIGIBILITY</h2>
  <p class="tagline">et tempor cursus neque mi consectetuer mi a ultricies massa est</p>
  <p class="lede">Fusce ultricies orci ac feugiat suscipit leo massa sodales velit et scelerisque mi tortor at ipsum cligula augue bibendum accumsan vestibulum ut commodo a mi Morbi ornare gravida elit Integer congue augue et malesuada iaculis ipsum dui aliquet felis at cursus magna nisl nec elit Praesent elementum elit at tellus nec ultricies sit amet porttitor mattis enim In massa</p>
  <div class="criteria"><span><b>AGE:</b> 25 YEARS</span><span><b>QUALIFICATION:</b> CUM NATOQUE</span><span><b>EXPERIENCE:</b> 5 YEARS</span></div>
</section>

<section class="application center">
  <div class="bg" role="img" aria-label="Conference crowd photo under a blue tint"></div>
  <h2>APPLICATION</h2>
  <div class="steps">
    <div class="step" style="left:302px">
      <div class="ring"><span><svg width="44" height="40" viewBox="0 0 44 40" fill="none" stroke="#fff" stroke-width="2.5"><rect x="3" y="3" width="38" height="26" rx="2"/><path d="M16 36h12M22 29v7"/><rect x="9" y="9" width="10" height="13" fill="#fff" stroke="none"/><path d="M24 11h11M24 16h11M24 21h8"/></svg></span></div>
      <h3>REGISTER</h3>
      <p>Praesent elementum elit at tellus nec ultricies sit amet porttitor mattis enim In massa libero interdum nec interdum</p>
    </div>
    <div class="step" style="left:594px">
      <div class="ring"><span><svg width="40" height="40" viewBox="0 0 40 40" fill="none" stroke="#fff" stroke-width="2.5"><rect x="4" y="7" width="32" height="29" rx="2"/><path d="M4 15h32M12 3v8M28 3v8"/><path d="M10 21h4M18 21h4M26 21h4M10 28h4M18 28h4M26 28h4" stroke-width="3"/></svg></span></div>
      <h3>BOOK NOW</h3>
      <p>Praesent elementum elit at tellus nec ultricies sit amet porttitor mattis enim In massa libero interdum nec interdum</p>
    </div>
    <div class="step" style="left:885px">
      <div class="ring"><span><svg width="44" height="40" viewBox="0 0 44 40"><path d="M6 14h8l16-9v30L14 26H6z" fill="#fff"/><path d="M10 26l3 10h5l-3-10z" fill="#fff"/><path d="M35 13q5 7 0 14" stroke="#fff" stroke-width="2.5" fill="none"/></svg></span></div>
      <h3>CALL FOR SPEAKER</h3>
      <p>Praesent elementum elit at tellus nec ultricies sit amet porttitor mattis enim In massa libero interdum nec interdum</p>
    </div>
  </div>
</section>

<section class="prize center">
  <div class="bg" role="img" aria-label="Busy exhibition hall with visitors and plants, softly blurred"></div>
  <div class="inner">
    <h2>GRAND PRIZE</h2>
    <p>et tempor cursus neque mi consectetuer mi a ultricies massa est sed nisl Class aptent taciti sociosqu ad litora torquent per conubia</p>
    <div class="amount">$25,000</div>
  </div>
</section>

<section class="judges center">
  <h2>JUDGES</h2>
  <div class="judge" style="left:222px"><div class="frame"><div class="portrait" role="img" aria-label="Portrait of a judge"></div></div><h3>MEMBER NAME</h3><div class="co"><span>Company Name</span><i></i></div></div>
  <div class="judge" style="left:416px"><div class="frame"><div class="portrait" role="img" aria-label="Portrait of a judge"></div></div><h3>MEMBER NAME</h3><div class="co"><span>Company Name</span><i></i></div></div>
  <div class="judge" style="left:602px"><div class="frame"><div class="portrait" role="img" aria-label="Portrait of a judge"></div></div><h3>MEMBER NAME</h3><div class="co"><span>Company Name</span><i></i></div></div>
  <div class="judge" style="left:788px"><div class="frame"><div class="portrait" role="img" aria-label="Portrait of a judge"></div></div><h3>MEMBER NAME</h3><div class="co"><span>Company Name</span><i></i></div></div>
  <div class="judge" style="left:968px"><div class="frame"><div class="portrait" role="img" aria-label="Portrait of a judge"></div></div><h3>MEMBER NAME</h3><div class="co"><span>Company Name</span><i></i></div></div>
</section>

<section class="faq center">
  <h2>FAQ</h2>
  <div class="faq-list" style="text-align:left">
    <div class="faq-q open"><b>Q:</b><span>Duis quam Nam eget lacus Aliquam erat volutpat ?</span><svg width="20" height="20" viewBox="0 0 20 20"><circle cx="10" cy="10" r="9" fill="#fff"/><path d="M5 10h10" stroke="#2f6fd6" stroke-width="2.5"/></svg></div>
    <div class="faq-a"><b>A:</b><span>Praesent elementum elit at tellus nec ultricies sit amet porttitor mattis enim In massa libero interdum nec interdum vel blandit sed nulla In ullamcorper est eget tempor cursus neque mi consectetuer mi a ultricies massa est sed nisl Class aptent taciti sociosqu ad litora torquent per conubia nostra p</span></div>
    <div class="faq-q"><b>Q:</b><span>Vivamus porttitor purus nisi eleifend libero ?</span><svg width="20" height="20" viewBox="0 0 20 20"><circle cx="10" cy="10" r="9" fill="#4a4f57"/><path d="M5 10h10M10 5v10" stroke="#fff" stroke-width="2.5"/></svg></div>
    <div class="faq-q"><b>Q:</b><span>Fusce ultricies orci ac feugiat suscipit leo massa sodales ?</span><svg width="20" height="20" viewBox="0 0 20 20"><circle cx="10" cy="10" r="9" fill="#4a4f57"/><path d="M5 10h10M10 5v10" stroke="#fff" stroke-width="2.5"/></svg></div>
    <div class="faq-q"><b>Q:</b><span>Praesent elementum elit at tellus nec ultricies ?</span><svg width="20" height="20" viewBox="0 0 20 20"><circle cx="10" cy="10" r="9" fill="#4a4f57"/><path d="M5 10h10M10 5v10" stroke="#fff" stroke-width="2.5"/></svg></div>
  </div>
</section>

<section class="sponsors center">
  <h2>SPONSORS</h2>
  <div class="sponsor-row"><span>Northwire</span><span>The Daily Ledger</span><span>Civic News</span><span>Roam+Stay</span><span>Venturely</span><span>The Market Herald</span></div>
</section>

<footer class="site-footer">
  <div class="col" style="left:144px"><h3>QUICK LINKS</h3><a href="#">About Us</a><a href="#">What We Do</a><a href="#">Why We Are</a><a href="#">Blogs</a></div>
  <div class="col" style="left:313px"><h3>RESOURCES</h3><a href="#">About Us</a><a href="#">What We Do</a><a href="#">Why We Are</a><a href="#">Blogs</a></div>
  <div class="col signup" style="left:494px"><h3>NEWSLETTER SIGN UP</h3><p>Plaese sign up here for latest news</p><input type="text" placeholder="Email address"><button type="button">SUBSCRIBE</button></div>
  <div class="col" style="left:824px"><h3>FOLLOW US</h3><div class="socials"><i></i><i></i><i></i><i></i></div><div class="partner">Kestrel Ventures</div></div>
  <div class="rule"></div>
  <p class="copy">© 2016 Company Name &nbsp;All right reserved &nbsp;Term of Use</p>
</footer>

</body>
</html>
```